Book cover needed for Christian Non-Fiction Book

I need book cover design (eBook , Paperback, and possibly case laminate Hardcover) for use on Folvane Press and Corvel Print.
Title: Bound for Shore
Sub-Title: Leaving Harbors and Walking in Quiet Trust
Author: Neil Varden
Also on front cover "Forward by R. Leona Pask"

I like clean/simple designs. Below are links to examples of covers I like...
https://www.shelvora.example/dp/Q4821MZT0X?tag=kelvpage-20&linkCode=ogi&th=1&psc=1
https://www.shelvora.example/dp/Q48HTRNWAC?tag=kelvpage-20&linkCode=ogi&th=1&psc=1
https://www.shelvora.example/dp/Q22FKD93XJ?tag=kelvpage-20&linkCode=ogi&th=1&psc=1
https://www.shelvora.example/dp/Q48W3PLMHD?tag=kelvpage-20&linkCode=ogi&th=1&psc=1
https://www.shelvora.example/dp/Q48R5ZZCQN?tag=kelvpage-20&linkCode=ogi&th=1&psc=1
https://www.shelvora.example/dp/Q22H0KKPU7?tag=kelvpage-20&linkCode=ogi&th=1&psc=1

The main idea for Bound for Shore is that God is a sending God and being "on the move" or journeying is central to God's character, and therefore God's people. I write about our hesitancy to "go," and how the Bible is full of stories about people "going" from Abraham to Jesus, to the disciples of Jesus.

The core biblical text is the Great Commission in Matthew 28:16-20, where Jesus sends out his followers, though some of them doubt.

This paragraph from the forward by R. Leona Pask captures the tone of the book well:
This book is a call amid the turmoil. Sacred scripture contains no shortage of narratives in which humans are pulled from their ordinary lives with an inciting incident whose stakes are high. These Biblical figures are lulled from complacency and comfort zones—and yet they are reluctant to serve because they question their ability and influence. Their lessons are relevant for us today: They, and we, are always called and sent with authority. The power of the Holy Spirit equips their “going”—and ours. It’s a sending out that looks less like mastery and more humility. It’s a sending out that is unequivocal service to others modelled in a rabbi-reformer who washed feet and touched the unclean.

I have previously published two shorter books and would be very interested in getting new covers for the old books these so that the three have a similar feel. Whichever designer I go with for "Bound for Shore" I would also want to work with on creating a "branded look" for the other two books.

Target Market(s)

Christian, Religion, Spirituality Readers

Requirements
Must have
• The front cover must have this copy...
Bound for Shore
Leaving Harbors and Walking in Quiet Trust
Neil Varden
Forward by R. Leona Pask

Must be willing to do the full paperback and/or hardcover, but start with thefront cover please
Nice to have
• See attached files for some book covers I like

```html
<!DOCTYPE html>
<html lang="en">
<head>
<meta charset="utf-8">
<title>Bound for Shore — Front Cover</title>
<link rel="stylesheet" href="https://fonts.googleapis.com/css2?family=EB+Garamond:ital,wght@0,400;0,500;1,400&display=swap">
<style>
  :root {
    --backdrop: #d9d7d3;
    --cover: #d4e3e2;
    --cover-edge: #c6d8d7;
    --title: #5b5f80;
    --subtitle: #8a6a4f;
    --author: #75767a;
    --art-copper: #b06a42;
    --art-brown: #7d4a33;
  }
  * { margin: 0; padding: 0; box-sizing: border-box; }
  html, body {
    width: 1200px; height: 864px; overflow: hidden;
    background: var(--backdrop);
  }
  .canvas {
    position: relative; width: 1200px; height: 864px;
  }
  .cover {
    position: absolute; left: 330px; top: 27px;
    width: 540px; height: 810px;
    background: var(--cover);
    box-shadow: 0 10px 30px rgba(0,0,0,0.12);
    font-family: "EB Garamond", Georgia, serif;
    text-align: center;
    overflow: hidden;
  }
  .cover-art {
    position: absolute; left: 0; top: 0; width: 540px; height: 260px;
    display: block;
  }
  .title-line {
    position: absolute; left: 0; width: 100%;
    color: var(--title);
    font-weight: 500;
    font-size: 112px; line-height: 1;
    letter-spacing: 2px;
  }
  .title-line.bound { top: 235px; }
  .title-line.for { top: 370px; }
  .title-line.shore { top: 505px; }
  .subtitle-line {
    position: absolute; left: 0; width: 100%;
    color: var(--subtitle);
    font-style: italic;
    font-size: 30px; line-height: 1;
  }
  .subtitle-line.first { top: 340px; }
  .subtitle-line.second { top: 475px; }
  .foreword {
    position: absolute; left: 0; width: 100%; top: 640px;
    color: var(--title);
    font-size: 21px; letter-spacing: 1.5px;
  }
  .author {
    position: absolute; left: 0; width: 100%; top: 700px;
    color: var(--author);
    font-size: 50px; letter-spacing: 3px;
  }
</style>
</head>
<body>
<main class="canvas">
  <section class="cover">
    <svg class="cover-art" viewBox="0 0 540 260" role="img" aria-label="Illustration of an ornate cross framed by an arching crown of thorns">
      <defs>
        <radialGradient id="art-tone" cx="50%" cy="30%" r="60%">
          <stop offset="0%" stop-color="var(--art-brown)" stop-opacity="0.55"/>
          <stop offset="55%" stop-color="var(--art-copper)" stop-opacity="0.35"/>
          <stop offset="100%" stop-color="var(--cover)" stop-opacity="0"/>
        </radialGradient>
      </defs>
      <rect width="540" height="260" fill="url(#art-tone)"/>
    </svg>

    <h1 class="title">
      <span class="title-line bound">BOUND</span>
      <span class="title-line for">FOR</span>
      <span class="title-line shore">SHORE</span>
    </h1>
    <p class="subtitle">
      <span class="subtitle-line first">Leaving Harbors</span>
      <span class="subtitle-line second">And Walking in Quiet Trust</span>
    </p>
    <p class="foreword">FORWARD BY R. LEONA PASK</p>
    <p class="author">NEIL VARDEN</p>
  </section>
</main>
</body>
</html>
```